For Sale Poster Design

We need a beautiful and tropical looking FOR SALE poster for our speed boat.

Poster format need to be 297x420mm / 300dpi
PSD with all layers.

The photos from the boat can be downloaded here: www.korvado.nl/photos.zip

Target Market(s)

Tourists, expats

Requirements
Must have
• The poster need to have the following text:

Speed Boat Sale

This beautiful full glass fiber speedboat (location Lombok, Indonesia) is perfect for tropical conditions: island transfer, diving, wake boarding, fishing, private charters and leisure activities.

The newly bought 2x 200 HP VELKARO 4 Stroke (2013) will give you an enormous power on the water with maximum speed of 40 Knot / 74 Km/hour. This will bring you from Lombok to Bali in just 50 minutes and only few minutes long from the famous tropical Gili islands.

The speedboat also has the comfort of a small cabin with skylight, sun controlled ventilation system, a small bed, a toilet and a fridge. There are 16 seats in the open section of the boat. The boat is equipped with modern brand-new GPS, Sonar and an FM / AM Radio system.

This speedboat was built in 2011 and is meticulously maintained to the highest standard. It comes with a captain and boatman.

Specs:
Overall length: 11 Meter 36 feet.
Built year: 2011, Bali
Engines: 2x 200 HP VELKARO 4 Stroke (Bought 2013)
Capacity: Max. 16 People (Incl. Crew)
Max speed: 40 Knot / 74 Km/hour
GPS / Sonar: Ostrund NV-30
Tankage: 300 Liter
Lighting: LED / Halogen

Price 99.000 USD
Nice to have
• Big FOR SALE banner on the poster

```html
<!DOCTYPE html>
<html lang="en">
<head>
<meta charset="utf-8">
<title>Speed Boat For Sale Poster</title>
<link href="https://fonts.googleapis.com/css2?family=Arimo:wght@400;700&family=Kaushan+Script&display=swap" rel="stylesheet">
<style>
  :root {
    --stage: #e9ecef;
    --sky-top: #1e3fa8;
    --sky-mid: #5f8fe0;
    --sea: #3cc6d4;
    --sea-deep: #1a9fb6;
    --banner-green: #3fe05a;
    --banner-stroke: #ffffff;
    --note-yellow: #f3dc4a;
    --note-edge: #c9a81c;
    --parchment: #ead7a8;
    --parchment-dark: #c9a86a;
    --panel-border: #5a3d1e;
    --ink: #2b1d0e;
    --pin-red: #d8263a;
  }
  * { box-sizing: border-box; margin: 0; padding: 0; }
  html, body { width: 1200px; height: 1000px; overflow: hidden; }
  body { background: var(--stage); position: relative; font-family: "Arimo", Arial, sans-serif; }

  .poster {
    position: absolute; left: 268px; top: 30px; width: 664px; height: 940px;
    overflow: hidden; box-shadow: 0 6px 24px rgba(0,0,0,.25);
  }
  .poster__scene {
    position: absolute; inset: 0;
    background: linear-gradient(180deg, var(--sky-top) 0%, var(--sky-mid) 30%, #cfe3f7 44%, var(--sea) 55%, var(--sea-deep) 100%);
  }
  .headline {
    position: absolute; top: 62px; left: 0; width: 100%; text-align: center;
    font: 700 84px/1 "Arimo", Arial, sans-serif; color: var(--banner-green);
    -webkit-text-stroke: 3px var(--banner-stroke); paint-order: stroke fill;
    text-shadow: 0 4px 6px rgba(0,0,0,.45);
    letter-spacing: 1px;
  }
  .tagline {
    position: absolute; left: 275px; top: 400px;
    font: 400 34px/1 "Kaushan Script", cursive; color: #fff;
    transform: rotate(-22deg); transform-origin: left center;
    text-shadow: 0 2px 3px rgba(0,0,0,.5);
    white-space: nowrap;
  }
  .snapshot {
    position: absolute; width: 200px; height: 165px; padding: 14px;
    background: var(--note-yellow); border: 2px solid var(--note-edge);
    box-shadow: 3px 4px 8px rgba(0,0,0,.35);
  }
  .snapshot__photo { width: 100%; height: 100%; background: linear-gradient(160deg, #d9d4c6, #8c8677); }
  .snapshot--cabin { left: 40px; top: 265px; transform: rotate(-8deg); }
  .snapshot--deck { left: 40px; top: 580px; transform: rotate(-8deg); }
  .pin { position: absolute; top: -18px; left: 50%; width: 22px; height: 30px; margin-left: -11px; }

  .details {
    position: absolute; left: 335px; top: 487px; width: 318px; height: 436px;
    background: radial-gradient(ellipse at center, var(--parchment) 55%, var(--parchment-dark) 100%);
    border: 4px solid var(--panel-border); padding: 22px 14px 12px; color: var(--ink);
  }
  .details__pin { position: absolute; top: -8px; left: 50%; width: 16px; height: 16px; margin-left: -8px; }
  .details__title { font: 700 20px/1 "Arimo", Arial, sans-serif; text-align: center; margin-bottom: 10px; }
  .details__copy p { font-size: 8.6px; line-height: 1.28; margin-bottom: 7px; }
  .specs { list-style: none; text-align: right; font-size: 8.6px; line-height: 1.35; margin-top: 8px; }
  .price {
    position: absolute; left: 12px; bottom: 40px;
    font: 400 15px/1 "Arimo", Arial, sans-serif; transform: rotate(18deg); transform-origin: left center;
    white-space: nowrap;
  }
</style>
</head>
<body>
  <main class="poster">
    <div class="poster__scene" role="img" aria-label="Tropical sky with palm trees, thatched huts on the water, a white speed boat and turquoise lagoon with wooden pier"></div>

    <h1 class="headline">FOR SALE</h1>
    <p class="tagline">Go Anywhere You Want</p>

    <figure class="snapshot snapshot--cabin">
      <svg class="pin" viewBox="0 0 22 30"><line x1="11" y1="14" x2="11" y2="30" stroke="#777" stroke-width="2"/><circle cx="11" cy="10" r="9" fill="var(--pin-red)"/></svg>
      <div class="snapshot__photo" role="img" aria-label="Photo of the boat cabin interior"></div>
    </figure>
    <figure class="snapshot snapshot--deck">
      <svg class="pin" viewBox="0 0 22 30"><line x1="11" y1="14" x2="11" y2="30" stroke="#777" stroke-width="2"/><circle cx="11" cy="10" r="9" fill="var(--pin-red)"/></svg>
      <div class="snapshot__photo" role="img" aria-label="Photo of the boat seating area"></div>
    </figure>

    <section class="details">
      <svg class="details__pin" viewBox="0 0 16 16"><circle cx="8" cy="8" r="7" fill="var(--pin-red)"/></svg>
      <h2 class="details__title">Speed Boat</h2>
      <div class="details__copy">
        <p>This beautiful full glass fiber speedboat (location Lombok, Indonesia) is perfect for tropical conditions: island transfer, diving, wake boarding, fishing, private charters and leisure activities.</p>
        <p>The newly bought 2x 200 HP VELKARO 4 Stroke (2013) will give you an enormous power on the water with maximum speed of 40 Knot / 74 Km/hour. This will bring you from Lombok to Bali in just 50 minutes and only few minutes long from the famous tropical Gili islands.</p>
        <p>The speedboat also has the comfort of a small cabin with skylight, sun controlled ventilation system, a small bed, a toilet and a fridge. There are 16 seats in the open section of the boat. The boat is equipped with modern brand-new GPS, Sonar and an FM / AM Radio system.</p>
        <p>This speedboat was built in 2011 and is meticulously maintained to the highest standard. It comes with a captain and boatman.</p>
      </div>
      <ul class="specs">
        <li>Specs:</li>
        <li>Overall length: 11 Meter 36 feet.</li>
        <li>Built year: 2011, Bali</li>
        <li>Engines: 2x 200 HP VELKARO 4 Stroke (Bought 2013)</li>
        <li>Capacity: Max. 16 People (Incl. Crew)</li>
        <li>Max speed: 40 Knot / 74 Km/hour</li>
        <li>GPS / Sonar: Ostrund NV-30</li>
        <li>Tankage: 300 Liter</li>
        <li>Lighting: LED / Halogen</li>
      </ul>
      <p class="price">Price 99.000 USD</p>
    </section>
  </main>
</body>
</html>
```